Trevolant Consulting Card Design

Create a card design for the company.

Target Market(s)

B2B

Industry/Entity Type

Management Consulting

Contact Information for Business Card

Name; Role; email; phone; website;

Colors
0555a3
3276b5
85abd2
cee9f5

```html
<!DOCTYPE html>
<html lang="en">
<head>
<meta charset="utf-8">
<title>Trevolant Consulting – Business Card</title>
<link href="https://fonts.googleapis.com/css2?family=Questrial&display=swap" rel="stylesheet">
<style>
  :root {
    --navy: #0555a3;
    --blue: #3276b5;
    --sky: #85abd2;
    --ice: #cee9f5;
    --paper: #fbfbfb;
    --grey: #8a8d91;
    --stage: #eceef1;
  }
  * { margin: 0; padding: 0; box-sizing: border-box; }
  html, body {
    width: 1200px;
    height: 1022px;
    overflow: hidden;
    background: var(--stage);
    font-family: "Questrial", "Century Gothic", sans-serif;
  }
  .card {
    position: absolute;
    left: 180px;
    top: 271px;
    width: 840px;
    height: 480px;
    background: var(--paper);
    box-shadow: 0 10px 30px rgba(0, 0, 0, 0.18);
    overflow: hidden;
  }
  .divider {
    position: absolute;
    top: 0;
    left: 452px;
    width: 6px;
    height: 100%;
    background: var(--navy);
  }
  .band {
    position: absolute;
    top: 0;
    left: 470px;
    right: 0;
    height: 100%;
    background: linear-gradient(160deg, var(--navy) 0%, var(--blue) 55%, #2f8ac9 100%);
  }
  .brand {
    position: absolute;
    left: 70px;
    top: 190px;
    display: flex;
    align-items: center;
    gap: 16px;
  }
  .brand-dot {
    width: 62px;
    height: 62px;
    border-radius: 50%;
    background: var(--blue);
    flex: none;
  }
  .brand-text { display: flex; flex-direction: column; }
  .brand-name {
    font-size: 54px;
    line-height: 1;
    color: var(--navy);
    letter-spacing: 0.5px;
  }
  .brand-tagline {
    margin-top: 6px;
    font-size: 13.5px;
    letter-spacing: 1.6px;
    color: var(--grey);
    white-space: nowrap;
  }
  .contacts {
    position: absolute;
    top: 48px;
    right: 40px;
    list-style: none;
    text-align: right;
    color: #ffffff;
    font-size: 19px;
  }
  .contacts li {
    display: flex;
    justify-content: flex-end;
    align-items: center;
    gap: 14px;
    height: 34px;
    white-space: nowrap;
  }
  .contacts svg { width: 15px; height: 15px; flex: none; }
  .holder {
    position: absolute;
    left: 510px;
    bottom: 44px;
    color: #ffffff;
  }
  .holder-name { font-size: 30px; line-height: 1.1; }
  .holder-role { font-size: 17px; color: var(--ice); margin-top: 4px; }
</style>
</head>
<body>
  <article class="card">
    <section class="brand">
      <span class="brand-dot"></span>
      <div class="brand-text">
        <span class="brand-name">trevolant</span>
        <span class="brand-tagline">ADVANCING YOUR STRATEGY</span>
      </div>
    </section>

    <div class="divider"></div>
    <div class="band"></div>

    <ul class="contacts">
      <li>+351 900 482 117
        <svg viewBox="0 0 16 16" aria-hidden="true"><path d="M4 1.5l2.3 3-1.4 1.6a8.5 8.5 0 0 0 5 5l1.6-1.4 3 2.3-1.6 2.2C8 14 2 8 1.8 3.1z" fill="none" stroke="#fff" stroke-width="1.3" stroke-linejoin="round"/></svg>
      </li>
      <li>tomas.ferreira@trevolant.com
        <svg viewBox="0 0 16 16" aria-hidden="true"><rect x="1.5" y="3.5" width="13" height="9" fill="none" stroke="#fff" stroke-width="1.3"/><path d="M1.5 3.5L8 9l6.5-5.5" fill="none" stroke="#fff" stroke-width="1.3"/></svg>
      </li>
      <li>www.trevolant.com
        <svg viewBox="0 0 16 16" aria-hidden="true"><circle cx="8" cy="8" r="6.3" fill="none" stroke="#fff" stroke-width="1.3"/><ellipse cx="8" cy="8" rx="2.7" ry="6.3" fill="none" stroke="#fff" stroke-width="1.1"/><path d="M1.7 8h12.6M2.8 4.8h10.4M2.8 11.2h10.4" stroke="#fff" stroke-width="1"/></svg>
      </li>
    </ul>

    <div class="holder">
      <div class="holder-name">Tomas Ferreira</div>
      <div class="holder-role">Partner</div>
    </div>
  </article>
</body>
</html>
```